TKR Engineering Pty Ltd

I have already had nox welding and fabrication cards made , my business has changed too TKR engineering Pty Ltd so I need my logo changed on the cards
one side have my logo then the other side have what we do.
front side logo and details
owner /operator : Curtis Halvorsen
email: tkr.works@examplemail.net
number: 0491537204
ABN: 52 604 381 927
ACN: 728 391 056
on back have in dot points what we do:
* structural steel erection
* precast panels
* site welding
*steel alteration & repair
* rigging & dogging
*labour hire
Contact Information for Business Card
all details in breif
Look and feel
Each slider illustrates characteristics of the customer's brand and the style your logo design should communicate.

```html
<!DOCTYPE html>
<html lang="en">
<head>
<meta charset="utf-8">
<title>TKR Engineering Pty Ltd – Business Cards</title>
<link rel="stylesheet" href="https://fonts.googleapis.com/css2?family=Montserrat:wght@400;500;700;800&display=swap">
<style>
  :root {
    --stage: #1c1c1f;
    --navy: #14223a;
    --red: #a53a34;
    --white: #ffffff;
    --ink: #14223a;
    --grey: #2c2f36;
  }
  * { box-sizing: border-box; margin: 0; padding: 0; }
  html, body {
    width: 1200px; height: 948px; overflow: hidden;
    background: var(--stage);
    font-family: "Montserrat", Arial, sans-serif;
  }
  .canvas {
    width: 1200px; height: 948px;
    display: flex; flex-direction: column;
    align-items: center; justify-content: center; gap: 44px;
  }
  .card {
    width: 700px; height: 400px;
    border-radius: 26px;
    display: grid;
    grid-template-columns: 360px 1px 1fr;
    align-items: center;
    padding: 0 50px 0 40px;
    box-shadow: 0 18px 40px rgba(0,0,0,.45);
  }
  .card--back { background: var(--navy); color: var(--white); }
  .card--front { background: var(--white); color: var(--grey); }

  .brand {
    display: flex; align-items: center; gap: 16px;
    justify-content: center;
  }
  .brand__dot {
    width: 22px; height: 22px; border-radius: 50%;
    background: var(--red); flex: none;
  }
  .brand__name {
    font-weight: 800; font-size: 27px; line-height: 1.15;
    letter-spacing: .5px; text-transform: uppercase;
    width: 220px;
  }
  .card--back .brand__name { color: var(--white); }
  .card--front .brand__name { color: var(--ink); }

  .divider { width: 1px; height: 200px; }
  .card--back .divider { background: rgba(255,255,255,.7); }
  .card--front .divider { background: var(--red); }

  .services { padding-left: 40px; }
  .services__title {
    color: var(--red); font-weight: 700; font-size: 17px;
    letter-spacing: 1px; margin-bottom: 10px;
  }
  .services__list { list-style: none; }
  .services__item {
    font-size: 17px; font-weight: 500; line-height: 1.75;
    display: flex; align-items: center; gap: 12px;
  }
  .services__item::before {
    content: ""; width: 6px; height: 6px; border-radius: 50%;
    background: var(--red); flex: none;
  }

  .contact { padding-left: 40px; }
  .contact__name { font-weight: 800; font-size: 26px; color: var(--ink); }
  .contact__role { font-size: 17px; margin-bottom: 18px; }
  .contact__reg { font-size: 16px; line-height: 1.6; margin-bottom: 16px; }
  .contact__line {
    font-size: 16px; line-height: 1.8;
    display: flex; align-items: center; gap: 10px;
  }
  .contact__icon { width: 15px; height: 15px; flex: none; }
</style>
</head>
<body>
<main class="canvas">

  <section class="card card--back" aria-label="Card back: services">
    <div class="brand">
      <span class="brand__dot"></span>
      <span class="brand__name">TKR Engineering Pty Ltd</span>
    </div>
    <span class="divider"></span>
    <div class="services">
      <h2 class="services__title">WE DO</h2>
      <ul class="services__list">
        <li class="services__item">Structural Steel Erection</li>
        <li class="services__item">Precast Panels</li>
        <li class="services__item">Site Welding</li>
        <li class="services__item">Steel Alteration &amp; Repair</li>
        <li class="services__item">Rigging &amp; Dogging</li>
        <li class="services__item">Labour Hire</li>
      </ul>
    </div>
  </section>

  <section class="card card--front" aria-label="Card front: contact details">
    <div class="brand">
      <span class="brand__dot"></span>
      <span class="brand__name">TKR Engineering Pty Ltd</span>
    </div>
    <span class="divider"></span>
    <div class="contact">
      <h1 class="contact__name">Curtis Halvorsen</h1>
      <p class="contact__role">Owner /Operator</p>
      <p class="contact__reg">ABN: 52 604 381 927<br>ACN: 728 391 056</p>
      <p class="contact__line">
        <svg class="contact__icon" viewBox="0 0 24 24" aria-hidden="true"><path fill="#a53a34" d="M6.6 10.8a15.1 15.1 0 0 0 6.6 6.6l2.2-2.2c.3-.3.7-.4 1-.2 1.1.4 2.3.6 3.6.6.6 0 1 .4 1 1V20c0 .6-.4 1-1 1A17 17 0 0 1 3 4c0-.6.4-1 1-1h3.5c.6 0 1 .4 1 1 0 1.3.2 2.5.6 3.6.1.3 0 .7-.2 1z"/></svg>
        0491537204
      </p>
      <p class="contact__line">
        <svg class="contact__icon" viewBox="0 0 24 24" aria-hidden="true"><path fill="#a53a34" d="M3 5h18a1 1 0 0 1 1 1v12a1 1 0 0 1-1 1H3a1 1 0 0 1-1-1V6a1 1 0 0 1 1-1zm9 7 8-5H4z"/></svg>
        tkr.works@examplemail.net
      </p>
    </div>
  </section>

</main>
</body>
</html>
```